Standard Company Posters / Notices

We have manufacturing sites, across the sites there are notices that managers put up, sometimes like a poster or door notice. These are not in any standard format or follow any standard layout. We wanted to create a notice template that could be adopted with layout guidance for all our internal notices. Some examples of the notices are below. We have three different sites so we would want to interchange the logo to suit the location, I have also added some images used for our values awards as examples of the look we like.

Target Market(s)

Employees

Industry/Entity Type

Food Manufacturing

Requirements
Must have
• Flexible for the site teams to amend to suit their needs.

```html
<!DOCTYPE html>
<html lang="en">
<head>
<meta charset="utf-8">
<title>Site Notice – Mobile Phones</title>
<link rel="stylesheet" href="https://fonts.googleapis.com/css2?family=League+Spartan:wght@700&family=Bebas+Neue&display=swap">
<style>
  :root {
    --paper: #ffffff;
    --ink: #000000;
    --header-grey: #666666;
    --ground-grey: #9e9e9e;
    --footer-grey: #666666;
  }
  html, body {
    margin: 0;
    padding: 0;
    width: 849px;
    height: 1200px;
    overflow: hidden;
    background: var(--paper);
  }
  .notice {
    display: block;
    width: 849px;
    height: 1200px;
  }
  .heading, .message, .signoff, .site-name {
    font-family: "League Spartan", "Arial", sans-serif;
    font-weight: 700;
  }
  .heading { fill: var(--paper); }
  .heading--main { font-size: 62px; }
  .heading--sub { font-size: 42px; }
  .message { fill: var(--ink); font-size: 58px; }
  .message--emphasis {
    font-family: "Bebas Neue", "Arial Narrow", sans-serif;
    font-weight: 400;
    font-size: 146px;
  }
  .message--authorised { font-size: 138px; }
  .signoff { fill: var(--footer-grey); }
  .signoff--title { font-size: 64px; }
  .signoff--name { font-size: 50px; }
  .site-name { fill: var(--footer-grey); font-size: 28px; }
  .site-mark { fill: var(--footer-grey); }
  .warning-shape, .header-band { fill: var(--header-grey); }
  .warning-mark { fill: var(--paper); }
  .message-panel { fill: var(--paper); stroke: var(--ink); stroke-width: 4; }
  .ground { fill: var(--ground-grey); }
  .ground-line { fill: none; stroke: var(--ink); stroke-width: 3; }
</style>
</head>
<body>
<svg class="notice" viewBox="0 0 849 1200" xmlns="http://www.w3.org/2000/svg">
  <!-- Header -->
  <g class="notice-header">
    <rect class="header-band" x="227" y="65" width="542" height="151"/>
    <path d="M191 37 L308 228 L98 228 Z" fill="var(--paper)" stroke="var(--paper)" stroke-width="22" stroke-linejoin="round"/>
    <path class="warning-shape" d="M191 37 L300 223 L82 223 Z" stroke="var(--header-grey)" stroke-width="12" stroke-linejoin="round"/>
    <path class="warning-mark" d="M181 100 Q181 96 185 96 L197 96 Q201 96 201 100 L196 164 Q195 169 191 169 Q187 169 186 164 Z"/>
    <circle class="warning-mark" cx="191" cy="189" r="11"/>
    <text class="heading heading--main" x="342" y="140" textLength="356" lengthAdjust="spacingAndGlyphs">ATTENTION</text>
    <text class="heading heading--sub" x="432" y="186" textLength="175" lengthAdjust="spacingAndGlyphs">PLEASE!</text>
  </g>

  <!-- Message panel -->
  <path class="message-panel" d="M83 1004 L83 368 Q83 292 160 292 L692 292 Q776 292 776 376 L776 1004 Z"/>
  <g class="message-text">
    <text class="message" x="132" y="428" textLength="591" lengthAdjust="spacingAndGlyphs">MOBILE PHONES ARE</text>
    <text class="message message--emphasis" x="163" y="550" textLength="526" lengthAdjust="spacingAndGlyphs">PROHIBITED</text>
    <text class="message" x="252" y="614" textLength="356" lengthAdjust="spacingAndGlyphs">IN THIS AREA</text>
    <text class="message" x="192" y="676" textLength="471" lengthAdjust="spacingAndGlyphs">UNLESS YOU ARE</text>
    <text class="message message--emphasis message--authorised" x="158" y="793" textLength="540" lengthAdjust="spacingAndGlyphs">AUTHORISED</text>
    <text class="message" x="252" y="851" textLength="348" lengthAdjust="spacingAndGlyphs">AND ON THE</text>
    <text class="message" x="170" y="913" textLength="521" lengthAdjust="spacingAndGlyphs">CONCESSION LIST!</text>
  </g>

  <!-- Ground band -->
  <path class="ground" d="M0 1002 L424 1018 L849 1002 L849 1033 L0 1033 Z"/>
  <path class="ground-line" d="M0 1002 L424 1018 L849 1002"/>

  <!-- Sign-off -->
  <g class="notice-footer">
    <text class="signoff signoff--title" x="140" y="1106" textLength="341" lengthAdjust="spacingAndGlyphs">SIGNED BY:</text>
    <text class="signoff signoff--name" x="140" y="1176" textLength="338" lengthAdjust="spacingAndGlyphs">MANAGEMENT</text>
    <rect class="site-mark" x="531" y="1104" width="22" height="22"/>
    <text class="site-name" x="565" y="1126">CARNFORD FOODS</text>
  </g>
</svg>
</body>
</html>
```